International Educational/Tuition/Learning Center

Company Background:
- Business card for a educational/tuition/learning center that provides supplementary lessons for students in Grade 7 to 12 ( Secondary and JC syllabus in the GCE 'O' and GCE 'A' level context but not limited to these. Future plans will be to cater for SAT, IB and HSCs programs.
- Name of company is called "THE QUILL AND LANTERN".
- Vision is to complement the basic principles of the rote learning culture and value-add by training the students to think out of the box and preserve creativity.
- To re-define and retain the value of the learning process.

Sketch Design:
- Simple and classy design that is mainly white-based with tinge of refreshing bright lime green.
- "New Age" simple and classy design that appeals to teenagers and young adults.
- Logo design to reinforce the vision of company.

Rough idea of what we have in mind but pls do not let this restrict your creativity:
- White and bright green base
- 2 sided print
- Front with simple information of Name and Designation as well as de-bossed/letterpressed print
- Details of on reverse side
- Contact details can be categorized as " find me" - address, "call me" - contact number , "email me" - email address, " Find out more"- website.

Information:

Name: Darel K Thuam
Title: Managing Director
Address: 41 Pelham Crescent, #07-15, Singapore 654321
Contact: +65 91234056
Email: darelthuam@mailvesta.com
Website: www.qnl-tutor.com

Thank you all in advance! Looking forward to some amazing designs from all you talented folks!
Updates

hi all,

have updated the projected to a guranteed status from the initial refundable status.

Thanks 

Dear designers,

I've included more info into the brief on design elements to include. 

Thanks for your participation and efforts!

Cheers!

Target Market(s)

young parents with school going children

Industry/Entity Type

Training

Requirements
Must have
• debossed/letterpressed logo
feel free to be creative with ur designs!
Nice to have
• round edges
Logo/name could have some elements of education/knowledge/path-to-learning incorporated in the design concept

```html
<!DOCTYPE html>
<html lang="en">
<head>
<meta charset="utf-8">
<title>The Quill and Lantern – Business Card</title>
<link rel="stylesheet" href="https://fonts.googleapis.com/css2?family=Arvo:wght@400;700&display=swap">
<style>
  :root {
    --page: #6f6f6f;
    --wood-dark: #3a1f14;
    --wood-mid: #5a3221;
    --wood-light: #6b3d28;
    --board: #3a3a3a;
    --board-edge: #2e2e2e;
    --chalk: #e9e9e6;
    --chalk-soft: #d6d6d2;
  }
  * { box-sizing: border-box; margin: 0; padding: 0; }
  html, body {
    width: 1200px;
    height: 1200px;
    overflow: hidden;
    background: var(--page);
  }
  .sheet {
    width: 1200px;
    height: 1200px;
    display: flex;
    flex-direction: column;
    align-items: center;
    justify-content: center;
    gap: 60px;
  }
  .card {
    width: 900px;
    height: 514px;
    padding: 24px;
    background: linear-gradient(135deg, var(--wood-light), var(--wood-mid) 45%, var(--wood-dark));
    border-radius: 4px;
    box-shadow: 0 10px 24px rgba(0,0,0,.35);
  }
  .board {
    width: 100%;
    height: 100%;
    background: radial-gradient(ellipse at 50% 40%, var(--board) 0%, var(--board-edge) 100%);
    position: relative;
    color: var(--chalk);
    font-family: "Arvo", Georgia, serif;
    font-weight: 700;
  }
  .card-front .board {
    display: flex;
    align-items: center;
    justify-content: center;
  }
  .brand-name {
    text-align: center;
    font-size: 58px;
    line-height: 1.08;
    letter-spacing: 4px;
    text-transform: uppercase;
    transform: translateX(10px);
  }
  .person {
    position: absolute;
    top: 72px;
    left: 0;
    width: 100%;
    text-align: center;
    transform: translateX(18px);
  }
  .person-name {
    font-size: 34px;
    letter-spacing: 3px;
    text-transform: uppercase;
    line-height: 1;
  }
  .person-title {
    font-size: 17px;
    letter-spacing: 1px;
    color: var(--chalk-soft);
    margin-top: 6px;
  }
  .contacts {
    position: absolute;
    top: 178px;
    left: 200px;
    list-style: none;
  }
  .contact {
    display: flex;
    align-items: flex-start;
    gap: 18px;
    font-size: 22px;
    line-height: 30px;
    letter-spacing: 1.5px;
    margin-bottom: 18px;
  }
  .contact-icon {
    width: 30px;
    height: 30px;
    flex: 0 0 30px;
    fill: none;
    stroke: var(--chalk);
    stroke-width: 2.4;
    stroke-linejoin: round;
    stroke-linecap: round;
  }
</style>
</head>
<body>
<main class="sheet">

  <section class="card card-front" aria-label="Card front">
    <div class="board">
      <h1 class="brand-name">The Quill<br>and Lantern</h1>
    </div>
  </section>

  <section class="card card-back" aria-label="Card back">
    <div class="board">
      <header class="person">
        <h2 class="person-name">Darel K. Thuam</h2>
        <p class="person-title">Managing Director</p>
      </header>
      <ul class="contacts">
        <li class="contact">
          <svg class="contact-icon" viewBox="0 0 30 30" aria-hidden="true"><path d="M4 15 L15 5 L26 15 M8 12 V25 H22 V12 M13 25 V18 H17 V25"/></svg>
          <span>41 Pelham Crescent, #07-15,<br>Singapore 654321</span>
        </li>
        <li class="contact">
          <svg class="contact-icon" viewBox="0 0 30 30" aria-hidden="true"><path d="M9 5 L13 10 L10.5 13 C12 17 14 19 17 20.5 L20 18 L25 22 L22 26 C13 25 6 18 5 9 Z"/></svg>
          <span>+65 91234056</span>
        </li>
        <li class="contact">
          <svg class="contact-icon" viewBox="0 0 30 30" aria-hidden="true"><path d="M4 8 H26 V23 H4 Z M4 8 L15 17 L26 8"/></svg>
          <span>darelthuam@mailvesta.com</span>
        </li>
        <li class="contact">
          <svg class="contact-icon" viewBox="0 0 30 30" aria-hidden="true"><path d="M4 6 H26 V20 H4 Z M15 20 V25 M10 25 H20"/></svg>
          <span>www.qnl-tutor.com</span>
        </li>
      </ul>
    </div>
  </section>

</main>
</body>
</html>
```